Logo and Business Card Design

We are macadamia farmers with a network of operations able to deliver macadamia nuts to you!
Be it wholesale or retail supply, our production capacity, network of farms and processing facilities is able to provide reliable and secure supply of macadamia products.
We have a network of owned and contract production macadamia farms located throughout Queensland and New South Wales. Our farms are located in the lush green hinterland area of Northern New south wales and the rich and productive farmlands of the Burnett area of southern Queensland. We pride ourselves on our environmentally sensitive production systems, the ownership and pride in which our network of farmers care for their orchards and the food we produce. Collectively our farms deliver to processing facilities able to provide macadamia nut in shell and kernel in wholesale and retail quantities.
Our point of difference is our integrated supply chain, delivering paddock to plate capacity.
The enterprise is a true network in that we have combined production, processing and marketing expertise into a one stop shop!
Our design should communicate our network capacity, we are a food producer which is respectful of the land and the environment in which we operate.
Our focus is Macadamia nut production, we farm and process Macadamia's where they are a native tree.

The draft design concept we feel is too mechanical and sterile, its time for something fresh and exciting!

Environment

Pell Orchard Pty. Ltd
An Integrated Macadamia production Enterprise.

```html
<!DOCTYPE html>
<html lang="en">
<head>
<meta charset="utf-8">
<title>Pell Orchard – Business Card</title>
<link href="https://fonts.googleapis.com/css2?family=Tenor+Sans&display=swap" rel="stylesheet">
<style>
  :root {
    --backdrop: #efefef;
    --card-white: #ffffff;
    --ink: #151515;
    --brand-brown: #3b2427;
    --ring-green: #2e5631;
    --leaf-dark: #2f3a2c;
    --leaf-mid: #4d5b45;
    --leaf-light: #6f7c64;
  }
  * { box-sizing: border-box; margin: 0; padding: 0; }
  html, body {
    width: 1200px;
    height: 800px;
    overflow: hidden;
    background: var(--backdrop);
    font-family: "Tenor Sans", "Optima", sans-serif;
  }
  .stage {
    position: relative;
    width: 1200px;
    height: 800px;
    display: flex;
    align-items: center;
    justify-content: center;
    gap: 60px;
  }
  .card {
    width: 510px;
    height: 292px;
    position: relative;
    overflow: hidden;
    box-shadow: 0 2px 6px rgba(0,0,0,0.18);
  }
  .card--back {
    background: var(--card-white);
    display: flex;
    flex-direction: column;
    align-items: center;
    justify-content: center;
    text-align: center;
    color: var(--ink);
  }
  .card__company {
    font-size: 19px;
    line-height: 1.25;
  }
  .card__tagline {
    font-size: 19px;
    line-height: 1.25;
  }
  .card--front {
    background: var(--leaf-dark);
  }
  .orchard-photo {
    position: absolute;
    inset: 0;
    background:
      radial-gradient(ellipse at 25% 40%, var(--leaf-light) 0%, transparent 45%),
      radial-gradient(ellipse at 80% 65%, var(--leaf-mid) 0%, transparent 50%),
      linear-gradient(135deg, var(--leaf-mid) 0%, var(--leaf-dark) 60%, #262d24 100%);
  }
  .brand-seal {
    position: absolute;
    left: 50%;
    top: 50%;
    width: 176px;
    height: 176px;
    transform: translate(-50%, -50%);
    border-radius: 50%;
    background: var(--card-white);
    border: 8px solid var(--ring-green);
    display: flex;
    flex-direction: column;
    align-items: center;
    justify-content: center;
    gap: 10px;
  }
  .brand-seal__dot {
    width: 22px;
    height: 22px;
    border-radius: 50%;
    background: var(--ring-green);
  }
  .brand-seal__name {
    font-size: 22px;
    color: var(--brand-brown);
    white-space: nowrap;
  }
</style>
</head>
<body>
  <main class="stage">
    <section class="card card--back">
      <p class="card__company">Pell Orchard Pty. Ltd</p>
      <p class="card__tagline">An Integrated Macadamia production Enterprise.</p>
    </section>
    <section class="card card--front">
      <div class="orchard-photo" role="img" aria-label="Photograph of a macadamia tree branch with green leaves and nuts in their husks, darkened"></div>
      <div class="brand-seal">
        <span class="brand-seal__dot"></span>
        <span class="brand-seal__name">Pell Orchard</span>
      </div>
    </section>
  </main>
</body>
</html>
```